Satin Decor Paint Label

We will have three different sizes for this label but the dimensions for the medium size are 2" tall by 11.75'' wide. Please work off that.

Our colors are typically black and white but feel free to incorporate silver, gold, bronze or any combination. We would like to see multiple color variations of your designs.

General Info needed on label:
2736
Coatings
Interior Decor Paint
Furniture, Trim, Cabinets
Acrylic Waterborne Urethane
Satin Finish
16 FL. OZ. - 473 mL
````````````````````````````````````````````````````````````````````````````````````````````
Your design does not have to be the same as the one in the attached image.

You can put Satin Finish or Interior Decor Paint or something else going vertically up the side.

The label will be on a container like the the one in the attached image. Please have your design work on the same container.

```html
<!DOCTYPE html>
<html lang="en">
<head>
<meta charset="UTF-8">
<title>2736 Coatings – Satin Decor Paint Label</title>
<link href="https://fonts.googleapis.com/css2?family=Montserrat:wght@400;500;700&display=swap" rel="stylesheet">
<style>
  :root {
    --ink: #0a0a0a;
    --paper: #ffffff;
    --backdrop: #ffffff;
    --shadow: rgba(0, 0, 0, 0.55);
  }
  html, body {
    margin: 0;
    padding: 0;
    width: 1200px;
    height: 384px;
    overflow: hidden;
    background: var(--backdrop);
  }
  .canvas {
    position: relative;
    width: 1200px;
    height: 384px;
  }
  .label {
    position: absolute;
    left: 45px;
    top: 87px;
    width: 1111px;
    height: 204px;
    background: var(--paper);
    box-shadow: 6px 8px 8px var(--shadow);
    color: var(--ink);
    font-family: "Montserrat", sans-serif;
  }
  .finish-vertical {
    position: absolute;
    left: 417px;
    top: 102px;
    transform: translate(-50%, -50%) rotate(-90deg);
    white-space: nowrap;
    font-size: 27px;
    font-weight: 400;
    letter-spacing: 0.2px;
  }
  .finish-vertical strong { font-weight: 700; }
  .brand-block {
    position: absolute;
    left: 569px;
    top: 0;
    width: 0;
  }
  .brand-block > * {
    position: absolute;
    left: 0;
    transform: translateX(-50%);
    white-space: nowrap;
    margin: 0;
    text-align: center;
    line-height: 1;
  }
  .brand-name-number {
    top: 10px;
    font-size: 72px;
    font-weight: 500;
  }
  .brand-name-word {
    top: 92px;
    font-size: 22px;
    font-weight: 500;
    letter-spacing: 1px;
  }
  .product-name {
    top: 122px;
    font-size: 16.5px;
    font-weight: 500;
  }
  .product-details {
    top: 145px;
    font-size: 11px;
    font-weight: 400;
    line-height: 12.5px;
  }
  .volume {
    top: 177px;
    font-size: 8.5px;
    font-weight: 400;
  }
</style>
</head>
<body>
<div class="canvas">
  <section class="label">
    <div class="finish-vertical"><strong>Satin</strong> Finish</div>
    <div class="brand-block">
      <h1 class="brand-name-number">2736</h1>
      <div class="brand-name-word">COATINGS</div>
      <h2 class="product-name">Interior Decor Paint</h2>
      <p class="product-details">Acrylic Waterborne Urethane<br>Furniture - Trim - Cabinets</p>
      <p class="volume">16 FL. OZ. - 473 mL</p>
    </div>
  </section>
</div>
</body>
</html>
```